QWB Collection and Shipping Info Sheet

I need to convert an existing rather plain-looking MS Word doc (see attached file Fecal Sample Collection and Shipping Information V2.0.doc) into a visually appealing, professional-looking doc that reflects my current brand’s look and feel (Retail Kit Cover V1.8.pdf). At the same time, I am open to looking at improving on my brand’s look.

Target Market(s)

Horse owners, Barn Managers, Equine Veterinarians

Industry/Entity Type

Horseback Riding

Font styles to use
Sans Serif

Requirements
Must have
• Must be able to fit attached content on 2 pages (1 double signed 8x11 pdf - NOT a trifold doc). Must use Pasture Vial Labs brand standards for following colors listed:
• - lime green color: C: 75 Y: 100 or R 57 G 181 B 74 (not shown in attached file)
• - bold font is Helvetica Compressed
• - body copy (paragraphs) is Helvetica Medium
• - RGB equivalent of red is #ED1C24, which is the mix R 237, G 28, B 36
• However feel free to add other colors (e.g, golds, yellows, greys. etc.)
Nice to have
• I would like the design to be eye-catching, yet easy to read because it is a step-by-step instruction sheet. Feel free to use Icons. I have several more documents that also require updating, so I would prefer the look and feel of this doc to be transferable to other similar docs (e.g., FAQs, product descriptions, sales flyers.)
Should not have
• Do not change the written content or the order of the content. This is NOT a trifold doc.

```html
<!DOCTYPE html>
<html lang="en">
<head>
<meta charset="utf-8">
<title>QWB Collection and Shipping Info Sheet</title>
<link rel="stylesheet" href="https://fonts.googleapis.com/css2?family=Roboto+Condensed:wght@400;700&family=Arimo:wght@400;700&display=swap">
<style>
  :root {
    --brand-red: #ed1c24;
    --deep-red: #b3141a;
    --ink: #1a1a1a;
    --panel-dark: #161616;
    --paper: #ffffff;
    --stage: #d9d6d2;
    --grey-text: #3b3b3b;
    --photo-light: #bdbdbd;
    --photo-dark: #5a5a5a;
  }
  * { box-sizing: border-box; margin: 0; padding: 0; }
  html, body { width: 1200px; height: 770px; overflow: hidden; }
  body {
    background: var(--stage);
    font-family: "Arimo", Arial, sans-serif;
    position: relative;
  }
  .sheet {
    position: absolute;
    top: 15px;
    width: 570px;
    height: 740px;
    background: var(--paper);
    overflow: hidden;
    box-shadow: 0 4px 14px rgba(0,0,0,.25);
  }
  .sheet--front { left: 20px; }
  .sheet--back { left: 610px; }

  /* photo placeholders */
  .photo {
    position: absolute;
    background: linear-gradient(160deg, var(--photo-light), var(--photo-dark));
  }
  .photo--rider { left: 0; top: 0; width: 330px; height: 695px; }
  .photo--horse {
    left: 285px; top: 0; width: 285px; height: 360px;
    clip-path: polygon(0 0, 100% 0, 100% 78%, 0 100%);
  }

  .shapes { position: absolute; inset: 0; pointer-events: none; }

  /* brand mark */
  .brand {
    position: absolute;
    display: flex;
    align-items: center;
    gap: 6px;
    right: 16px;
    top: 18px;
  }
  .brand__dot {
    width: 62px; height: 62px; border-radius: 50%;
    background: var(--brand-red);
  }
  .brand__name {
    font-family: "Roboto Condensed", Arial, sans-serif;
    font-weight: 700;
    font-size: 14px;
    line-height: 1.05;
    color: var(--ink);
    text-transform: uppercase;
    width: 64px;
  }

  .tagline {
    position: absolute;
    right: 16px;
    top: 118px;
    text-align: right;
    font-family: "Roboto Condensed", Arial, sans-serif;
    font-size: 26px;
    line-height: 1.05;
    color: var(--ink);
    padding-bottom: 6px;
    border-bottom: 2px solid var(--brand-red);
  }

  .hero-title {
    position: absolute;
    left: 12px;
    top: 340px;
    width: 290px;
    color: #fff;
  }
  .hero-title h1 {
    font-family: "Roboto Condensed", Arial, sans-serif;
    font-weight: 700;
    font-size: 29px;
    line-height: 1.13;
    text-transform: uppercase;
  }
  .hero-title p {
    margin-top: 8px;
    font-size: 10px;
    line-height: 1.35;
  }
  .hero-title .hero-link {
    display: inline-block;
    margin-top: 2px;
    background: var(--ink);
    color: #fff;
    padding: 2px 6px;
    font-size: 10px;
  }

  /* step banners — front */
  .step-bar {
    position: absolute;
    left: 355px;
    width: 215px;
    height: 28px;
    background: var(--ink);
    clip-path: polygon(8% 0, 100% 0, 100% 100%, 0 100%);
    color: #fff;
    font-family: "Roboto Condensed", Arial, sans-serif;
    font-size: 18px;
    text-align: right;
    padding: 3px 12px 0 0;
  }
  .step-icon {
    position: absolute;
    width: 34px; height: 34px;
    border-radius: 50%;
    background: var(--brand-red);
    border: 2px solid #fff;
    display: flex; align-items: center; justify-content: center;
  }
  .step-icon svg { width: 18px; height: 18px; }
  .step-icon--light { background: #fff; border-color: var(--ink); }

  .step-copy {
    position: absolute;
    font-size: 8.6px;
    line-height: 1.36;
    color: var(--grey-text);
    text-align: justify;
  }
  .step-copy--right { text-align: right; }
  .step-copy .accent { color: var(--brand-red); }
  .kit-list { list-style: none; margin-top: 6px; text-align: right; }
  .kit-list li { margin-bottom: 4px; }
  .kit-list li::after {
    content: "";
    display: inline-block;
    width: 7px; height: 7px;
    border-radius: 50%;
    background: var(--brand-red);
    margin-left: 5px;
    vertical-align: -1px;
  }

  /* back sheet */
  .steps-column {
    position: absolute;
    left: 0; top: 0;
    width: 285px; height: 695px;
    background: var(--panel-dark);
  }
  .steps-column h2 {
    position: absolute;
    left: 14px; top: 12px;
    color: #fff;
    font-family: "Roboto Condensed", Arial, sans-serif;
    font-weight: 700;
    font-size: 19px;
  }
  .step-tab {
    position: absolute;
    left: 0;
    width: 205px;
    height: 26px;
    background: var(--brand-red);
    clip-path: polygon(0 0, 100% 0, 94% 100%, 0 100%);
    color: #fff;
    font-family: "Roboto Condensed", Arial, sans-serif;
    font-size: 17px;
    padding: 2px 0 0 20px;
  }
  .steps-column .step-copy { color: #e8e8e8; left: 20px; width: 250px; font-size: 8.1px; line-height: 1.3; }
  .steps-column .lead { color: var(--brand-red); display: block; }

  .step-bar--back { left: 300px; width: 230px; clip-path: polygon(0 0, 94% 0, 100% 100%, 0 100%); text-align: left; padding-left: 20px; }

  .footer {
    position: absolute;
    left: 0; bottom: 0;
    width: 570px; height: 45px;
    background: var(--ink);
  }
  .footer__contact {
    position: absolute;
    left: 0; top: 0;
    width: 380px; height: 45px;
    background: var(--brand-red);
    clip-path: polygon(0 0, 96% 0, 100% 100%, 0 100%);
    color: #fff;
    font-size: 8.6px;
    line-height: 1.3;
    padding: 10px 0 0 12px;
  }
  .footer__web {
    position: absolute;
    right: 16px; top: 15px;
    color: #fff;
    font-size: 11px;
    display: flex; align-items: center; gap: 5px;
  }
  .footer__web::before {
    content: "";
    width: 8px; height: 8px;
    border: 1.5px solid #fff;
    border-radius: 50%;
  }
</style>
</head>
<body>

<!-- FRONT PAGE -->
<section class="sheet sheet--front">
  <div class="photo photo--rider" role="img" aria-label="Black and white photo of a rider jumping a horse, with horses galloping below"></div>
  <svg class="shapes" width="570" height="740" viewBox="0 0 570 740">
    <polygon points="0,110 330,430 0,695" fill="#ed1c24"/>
    <polygon points="210,330 330,430 210,560" fill="#b3141a" opacity=".55"/>
    <polygon points="300,300 345,430 300,560" fill="#ed1c24"/>
  </svg>

  <div class="brand">
    <span class="brand__dot"></span>
    <span class="brand__name">Pasture Vial Labs</span>
  </div>

  <div class="tagline">JUST SCOOP,<br>SEAL &amp; SEND</div>

  <div class="hero-title">
    <h1>How to<br>collect &amp; ship a<br>fecal sample</h1>
    <p>Everything you need to test your horse for internal parasitesis contained in the Pasture Vial Labs Fecal Test Kit.Additional kits are available at</p>
    <span class="hero-link">pasturevial-labs.example/products/qwb-kit</span>
  </div>

  <!-- Step 1 -->
  <div class="step-bar" style="top:212px">STEP 1</div>
  <div class="step-icon" style="left:370px;top:209px">
    <svg viewBox="0 0 18 18"><path d="M2 6l7-3 7 3v7l-7 3-7-3z" fill="#fff"/><path d="M2 6l7 3 7-3M9 9v7" stroke="#ed1c24" stroke-width="1.3" fill="none"/></svg>
  </div>
  <div class="step-copy step-copy--right" style="left:345px;top:252px;width:212px">
    Begin by removing the Pasture Vial Labs Kit contents from the packaging. Confirm that your Kit contains the following items:
    <ul class="kit-list">
      <li>1 Resealable Fecal Collection Bag</li>
      <li>1 Gel Refrigerant Pack</li>
      <li>1 Pre-Addressed Shipping Thermal Bubble Mailer</li>
      <li>1 Equine Parasite Collection &amp; Treatment Form</li>
    </ul>
  </div>

  <!-- Step 2 -->
  <div class="step-bar" style="top:400px">STEP 2</div>
  <div class="step-icon" style="left:370px;top:397px">
    <svg viewBox="0 0 18 18"><circle cx="9" cy="9" r="6" fill="none" stroke="#fff" stroke-width="1.6"/><path d="M8 6l6 5-3 .5 1.5 3-1.5.7-1.5-3L8 14z" fill="#fff"/></svg>
  </div>
  <div class="step-copy step-copy--right" style="left:345px;top:440px;width:212px">
    Complete the Equine Parasite Collection &amp; Treatment Form. A Step-by-Step Video is available at <span class="accent">pasturevial-labs.example/pages/collect-sample</span>. Fillout the form before you collect the sample. If you have any questions, call us at <span class="accent">555-204-7718</span> or email <span class="accent">mrowe@pasturevial-labs.example</span>
  </div>

  <!-- Step 3 -->
  <div class="step-bar" style="top:540px">STEP 3</div>
  <div class="step-icon" style="left:370px;top:537px">
    <svg viewBox="0 0 18 18" stroke="#fff" stroke-width="1.6" stroke-linecap="round"><path d="M9 2v14M3 5.5l12 7M3 12.5l12-7"/></svg>
  </div>
  <div class="step-copy step-copy--right" style="left:345px;top:580px;width:212px">
    Place the Gel Refrigerant Packin the freezer at least 12 hours prior to shipping your sample.The frozen gel packhelps keep the sample cool during shipping. If your sample is warm when you collect it, place it in the refrigerator to cool for at least 30 minutes before packaging it for shipping. Never freeze the fecal sample.
  </div>

  <footer class="footer">
    <div class="footer__contact">Any question? Email us at mrowe@pasturevial-labs.example or call 555-204-7718.<br>Please check pasturevial-labs.example/hours for store hours.</div>
    <div class="footer__web">www.pasturevial-labs.example</div>
  </footer>
</section>

<!-- BACK PAGE -->
<section class="sheet sheet--back">
  <div class="photo photo--horse" role="img" aria-label="Black and white photo of a horse trotting across a field"></div>
  <svg class="shapes" width="570" height="740" viewBox="0 0 570 740">
    <polygon points="285,205 410,290 285,375" fill="#ed1c24"/>
  </svg>

  <div class="brand">
    <span class="brand__dot"></span>
    <span class="brand__name">Pasture Vial Labs</span>
  </div>

  <div class="steps-column">
    <h2>JUST SCOOP, SEAL &amp; SEND</h2>

    <div class="step-tab" style="top:46px">STEP 4</div>
    <div class="step-icon step-icon--light" style="left:176px;top:42px">
      <svg viewBox="0 0 18 18"><path d="M3 9l6-6h6v6l-6 6z" fill="#1a1a1a"/><circle cx="12" cy="6" r="1.3" fill="#fff"/></svg>
    </div>
    <div class="step-copy" style="top:82px">
      <span class="lead">Label the FecalCollection Bag.</span>
      Using a ballpoint pen or permanent marker, write your horse's name and date of collection in the blank white space provided on the outside of the Fecal Collection Bag.
    </div>

    <div class="step-tab" style="top:148px">STEP 5</div>
    <div class="step-icon step-icon--light" style="left:176px;top:144px">
      <svg viewBox="0 0 18 18"><ellipse cx="9" cy="13" rx="7" ry="3" fill="#1a1a1a"/><ellipse cx="9" cy="9" rx="5" ry="2.6" fill="#1a1a1a"/><path d="M6 6c1-3 4-3 4-4 2 2 1 4-1 4z" fill="#1a1a1a"/></svg>
    </div>
    <div class="step-copy" style="top:184px">
      <span class="lead">Positively IdentifyYour Horse's Manure Pile.</span>
      Determine with certainty the fecal sample has come from your horse, if your horse cohabitates. If necessary, isolate your horse where you know you can collect a sample without doubt. If sending more than one sample, use one Fecal Collection Bag for each sample taken. (Never combine samples from different horses in the same bag if you are collecting samples for more than one horse.)
      <span class="lead" style="margin-top:6px">The manure sample must be fresh.</span>
      Ideally, collect the sample shortly after your horse has passed it. Parasitic matter deteriorates overtime,which affects the test results. Schedule collection of samples in the morning if possible. Avoid collecting a manure sample that contains dirt, shavings, grass, etc. Select the sample from the top ormiddle of the manure pile. Avoid taking the sample from the portion of the pile touching the ground to minimize potential contamination.
    </div>

    <div class="step-tab" style="top:392px">STEP 6</div>
    <div class="step-icon step-icon--light" style="left:176px;top:388px">
      <svg viewBox="0 0 18 18"><path d="M13 2l3 3-5 5-3-3z" fill="#1a1a1a"/><path d="M8 8l2 2-4 6-4-4z" fill="#1a1a1a"/></svg>
    </div>
    <div class="step-copy" style="top:428px">
      <span class="accent" style="color:#ed1c24">DIG IN!</span> Once you have identifiedyour horse's sample, turn the fecalcollection bag inside out. A Step-by-Step Video is available at <span class="accent" style="color:#ed1c24">pasturevial-labs.example/blog/why-our-sample-collection-bag-is-the-best</span>. With the label on the inside of the bag, place your hand inside thebag and collect the fecal nugget of choice.Ideally, the sample size should be larger than a golf ball but smaller than a tennis ball. Carefully return the bag right-side-out by using your other hand to pull the bag back over the hand grasping the sample.
    </div>

    <div class="step-tab" style="top:562px">STEP 7</div>
    <div class="step-icon step-icon--light" style="left:176px;top:558px">
      <svg viewBox="0 0 18 18" stroke="#1a1a1a" stroke-width="1.5"><circle cx="9" cy="9" r="4" fill="#1a1a1a"/><path d="M9 2v3M9 13v3M2 9h3M13 9h3M4 4l2 2M12 12l2 2M4 14l2-2M12 6l2-2"/></svg>
    </div>
    <div class="step-copy" style="top:598px">
      <span class="lead">Removeas muchair as possible and seal the Fecal Collection Bag securely.</span>
      Elimination of air from the fecal collection bag helps to preserve the sample and prevent sparasitic eggs from hatching. Parasite eggs are anaerobic (living in the absence of air or oxygen) and removing excess air from the bag keepsthem alive longer. Make certain the bag is completely sealed to avoid leakage.
    </div>
  </div>

  <!-- Step 8 -->
  <div class="step-bar step-bar--back" style="top:350px">STEP 8</div>
  <div class="step-icon" style="left:500px;top:346px">
    <svg viewBox="0 0 18 18"><rect x="3" y="4" width="12" height="10" fill="none" stroke="#fff" stroke-width="1.5"/><path d="M5 8h8M5 11h6" stroke="#fff" stroke-width="1.3"/></svg>
  </div>
  <div class="step-copy" style="left:302px;top:388px;width:250px;font-size:8.1px;line-height:1.3">
    <span class="accent">Place the sealed Fecal Collection Bag in the Pre-Addressed Shipping Thermal Bubble Mailer.</span> If you are not able to ship your sample on the same day it is collected, simply place the Pre-Addressed Shipping Thermal Bubble Mailer with the sample in the refrigerator (&lt;39 Fo), until you are ready to ship it. Remember, DO NOT FREEZE the sample. ONLY USE THE PASTURE VIAL LABS PACKAGING PROVIDED. DO NOT SUBSTITUTE.
  </div>

  <!-- Step 9 -->
  <div class="step-bar step-bar--back" style="top:486px">STEP 9</div>
  <div class="step-icon" style="left:500px;top:482px">
    <svg viewBox="0 0 18 18"><rect x="3" y="4" width="12" height="10" fill="none" stroke="#fff" stroke-width="1.5"/><path d="M5 8h8M5 11h6" stroke="#fff" stroke-width="1.3"/></svg>
  </div>
  <div class="step-copy" style="left:302px;top:524px;width:250px;font-size:8.1px;line-height:1.3">
    Immediately prior to shipping, retrieve the Gel Refrigerant Pack from the freezer and place it inside the Pre-Addressed Shipping Thermal Bubble Mailer,next tothe sealed Fecal Collection Bag. For the Lab to process your sample in a timely manner, ship the sample early in the week to ensure receipt by the Lab prior tothe weekend.It is highly recommended that your sample arrive at the lab within two days of its collection.
    <br><br>
    After the Lab receives your horse's fecal sample, a test will be performed to analyze and calculate your horse's parasite burden. You will receive a detailed report summarizing the type and number of eggs found in the sample. Depending on your preferences indicated on your Equine Parasite Collection &amp; Treatment Form, the results will be emailed or sent via US Postal Service.
  </div>

  <footer class="footer">
    <div class="footer__contact">Any question? Email us at mrowe@pasturevial-labs.example or call 555-204-7718.<br>Please check pasturevial-labs.example/hours for store hours.</div>
    <div class="footer__web">www.pasturevial-labs.example</div>
  </footer>
</section>

</body>
</html>
```